Health care finance company startup website design

This design brief is for Ledger Nest, a small start-up company dealing with an online health care (initially dental targeted with plans for medical market) financial suite of tools. My business partners and I are looking to have a website developed for our business model.

We have developed a professional logo and would like it incorporated into the site. We are open to modifications on the logo if needed to accomplish the right design.

Our concept is a clean, simple design with a professional polish and very up-to-date web presence. The functionality of the site is simple yet powerful and we would like it’s design to complement that (including anticipated css3/html5 effects for an added dimension of UI polish).

We would like to see a design mockup of the functional elements of our site as our home page. We would also be very interested to see how your design would flow into the other pages such as search for a loan, create a payment plan, make a payment, sign in, registration, contact us and learn more.

Regarding Functional Elements:

-Simplicity is king.

-The three main functions of the site are the focus. They will operate via a series of API’s to webservices on the back-end, making the front end field focused, though we hope to have it feel friendly and simple.
-Search for a loan
-Create a payment plan
-Make a payment

Other functions of the site include:

-Sign in module
-We plan to support Kindlebook Link, Vornix Authentication and TrellisKey so incorporating design for those options is a plus.

-Registration module
-Two service levels clients can register for, loans only or loans & payments
-The registration process should be divided into sections with navigation back and forth until a confirmation final screen with pdf generations and remaining “to-do items” listed.
-The registration information will be saved in our database and also auto-populate fields for PDF’s that will be generated from templates.
-The registration will send a confirmation email and support TrellisKey, Vornix Authentication and Kindlebook Link, so designs should take these programmatic features into account.

-Contact us
-This will emphasize digital forms of communication (email and form submitted contact request).

-Learn more
-Explanations/faqs/tutorials
-This will contain video demonstrations/screencasts of key functions of website features

Regarding Design Elements:
-We want to be “wow’d” and don’t mind a surprise that redefines what we thought we liked regarding design.
-The following examples indicate some of the color schemes we like and design elements we hope to incorporate.
-We also recognize there is no substitute for creativity and originality.

Favorite Website Design Examples:

http://www.joginmarla.example/
HD backgrounds are a plus.
These colors are great.
The bright splashes of blue, red and orange combined with black in these shades.
A predominant background of whitesmoke or beige.

https://tillbrook.example/
The HD backgrounds are sharp.
The look is very clean (though it has a slight Quince computers imitation).
The left to right “scrolling” is preferable to vertical scrolling.
Very pleasing to the eye.

http://www.quarryfilmworks.example/
Again, use of bright, vibrant HD graphics is exceptional.
The left to right scrolling navigation is slick and likely how we would like our services to flow.

http://latest.wanderpelmark.example/
Love the look, feel and concepts in this site’s design
Especially colors and “photography” elements.
Updates

We've seen a few common themes in various designs submitted so far and want to add a few suggestions as we enter the final week of our design contest.

We do not want any photos of healthcare professionals or close-ups of people (families or couples or individuals).  Although we are a health care company we don't want to fall into a cliche feel for our site.  Instead we would like either objects or abstract images that have depth and are high definition, spanning from edge to edge of the width of the screen. 

We prefer shades of grey for the base color scheme with highlights of bright colors.  Please refer to the examples on the brief and use those as the best guide of what we want.  Even SketchGuild's color scheme is closer to what we want than some of the submissions, so please take note of the "shades of grey" with splashes of bright accent colors.

We love the horizontal navigation bar like that seen in the quarry filmworks site and anticipate our final product using a similar transition between the functions of the site.

Good luck to you all.  We are still looking for that WOW factor and hoping to see something original, that breaks the traditional mold and has a feel like the examples posted.

```html
<!DOCTYPE html>
<html lang="en">
<head>
<meta charset="utf-8">
<title>Ledger Nest — Home</title>
<link rel="stylesheet" href="https://fonts.googleapis.com/css2?family=Open+Sans:ital,wght@0,400;0,600;0,700;1,400&family=PT+Sans:wght@400;700&display=swap">
<style>
  :root {
    --ink-dark: #14110d;
    --panel-brown: rgba(58, 44, 26, 0.82);
    --accent-orange: #f39a1f;
    --accent-amber: #f5b55c;
    --button-yellow: #f7b81c;
    --field-dark: #3b3b3b;
    --text-light: #f4efe6;
    --text-muted: #b8b0a2;
    --nav-sand: rgba(196, 176, 146, 0.82);
    --social-blue: #3c5a98;
    --social-blue-light: #5a79b8;
    --signin-cream: rgba(247, 240, 224, 0.94);
    --link-blue: #2b5aa8;
    --logo-navy: #1b2c4e;
    --logo-grey: #6a6a6a;
  }
  * { box-sizing: border-box; margin: 0; padding: 0; }
  html, body { width: 1200px; height: 860px; overflow: hidden; }
  body { font-family: "Open Sans", Arial, sans-serif; background: var(--ink-dark); position: relative; }

  .hero-backdrop {
    position: absolute; inset: 0;
    background: linear-gradient(180deg, #f6ecd2 0%, #eddcb4 22%, #c9a56d 38%, #7a5630 52%, #3b2a17 64%, #1c150e 76%, #120e0a 100%);
  }
  .abs { position: absolute; }

  .brand { left: 187px; top: 22px; display: flex; align-items: center; gap: 10px; }
  .brand-mark { width: 36px; height: 36px; background: var(--logo-navy); border-radius: 4px; }
  .brand-name { font-size: 27px; letter-spacing: 1px; color: var(--logo-grey); font-weight: 400; }

  .about-panel {
    left: 196px; top: 100px; width: 380px; height: 392px; overflow: hidden;
    background: var(--panel-brown); border-radius: 6px; padding: 17px 16px 0 16px;
  }
  .about-title { color: var(--accent-orange); font-size: 18px; font-weight: 400; letter-spacing: .5px; margin-bottom: 9px; line-height: 24px; }
  .about-copy { font-family: "PT Sans", Arial, sans-serif; color: #fff; font-size: 9.7px; line-height: 18px; text-align: justify; }

  .signin-panel {
    left: 838px; top: 15px; width: 167px; height: 234px;
    background: var(--signin-cream); border: 1px solid #d9ccb0; border-radius: 4px;
  }
  .signin-tabs { position: absolute; top: 4px; right: 8px; font-size: 11px; color: #333; display: flex; gap: 6px; }
  .signin-tabs .active { border: 1px solid #d9ccb0; border-bottom: none; padding: 0 6px; background: var(--signin-cream); }
  .field-light {
    position: absolute; left: 8px; width: 150px; height: 25px; background: #fff;
    border: 1px solid #ddd; border-radius: 3px; font-size: 8px; color: #666;
    display: flex; align-items: center; padding-left: 22px;
  }
  .field-light svg { position: absolute; left: 8px; }
  .forgot-link { position: absolute; left: 10px; top: 105px; font-size: 8px; color: var(--link-blue); text-decoration: underline; }
  .signin-button {
    position: absolute; left: 118px; top: 100px; width: 34px; height: 13px;
    background: var(--button-yellow); border-radius: 2px; font-size: 7px; text-align: center; line-height: 13px; color: #222;
  }
  .or-rule { position: absolute; left: 8px; top: 135px; width: 150px; border-top: 1px solid #9a927f; }
  .or-rule span { position: absolute; left: 62px; top: -6px; font-size: 7px; background: var(--signin-cream); padding: 0 3px; color: #555; }
  .social-button {
    position: absolute; left: 8px; width: 150px; height: 23px;
    background: linear-gradient(180deg, var(--social-blue-light), var(--social-blue));
    border: 1px solid #2d467a; color: #fff;
    font-family: "PT Sans", Arial, sans-serif; font-size: 11px; font-weight: 700; white-space: nowrap;
    display: flex; align-items: center; gap: 7px; padding-left: 3px;
  }
  .social-button i { width: 18px; height: 18px; background: rgba(255,255,255,.25); display: block; flex: none; }

  .service-nav {
    left: 176px; top: 535px; width: 831px; height: 102px;
    background: var(--nav-sand); border: 1px solid rgba(255,255,255,.35); border-radius: 3px;
  }
  .service-tab-active {
    left: 268px; top: 527px; width: 82px; height: 114px;
    background: var(--accent-amber); border-radius: 5px; box-shadow: 0 0 6px rgba(0,0,0,.3);
  }
  .service-item { position: absolute; top: 543px; width: 120px; text-align: center; font-weight: 700; font-size: 12.5px; line-height: 14px; color: #1a1714; }
  .service-icon { width: 45px; height: 45px; margin: 0 auto 6px; border-radius: 5px; display: flex; align-items: center; justify-content: center; }
  .icon-dark { background: linear-gradient(180deg, #4a4f55, #15181b); }
  .icon-light { background: linear-gradient(180deg, #ffffff, #d9d9d9); }
  .icon-brand { background: var(--logo-navy); }

  .footer-title { color: #fff; font-size: 15px; font-weight: 400; }
  .footer-brand { left: 176px; top: 657px; display: flex; align-items: center; gap: 6px; }
  .footer-brand .brand-mark { width: 24px; height: 24px; background: #8a8a8a; border-radius: 3px; }
  .footer-brand .brand-name { font-size: 18px; color: #8a8a8a; }
  .field-label { color: #ddd; font-size: 9.5px; }
  .field-dark { background: var(--field-dark); }
  .orange-button {
    background: var(--accent-orange); color: #fff; font-size: 11px; text-align: center; border-radius: 4px;
  }
  .column-rule { width: 1px; background: #3d3831; top: 665px; height: 154px; }

  .testimonial { left: 465px; width: 232px; font-size: 8.5px; color: #fff; line-height: 13px; }
  .testimonial-meta { display: flex; justify-content: space-between; font-style: italic; color: var(--accent-orange); padding: 0 10px 0 3px; }
  .testimonial-more { text-align: right; font-style: italic; color: var(--text-muted); padding-right: 10px; }
  .quote-mark { font-family: Georgia, serif; font-size: 30px; line-height: 30px; color: #5b544a; }

  .legal-line { left: 0; width: 1200px; top: 843px; text-align: center; font-size: 9.5px; color: #d8d2c6; }
</style>
</head>
<body>
  <div class="hero-backdrop" role="img" aria-label="Full-width photograph of a concert crowd with raised hands under warm stage light"></div>

  <header class="brand abs">
    <span class="brand-mark"></span>
    <span class="brand-name">LEDGER NEST</span>
  </header>

  <section class="about-panel abs">
    <h2 class="about-title">WHO WE ARE ?</h2>
    <p class="about-copy">Lorem Ipsum is simply dummy text of the printing and typesetting industry. Lorem Ipsum has been the industry's standard dummy text ever since the 1500s, when an unknown printer took a galley of type and scrambled it to make a type specimen book. It has survived not only five centuries, but also the leap into electronic typesetting, remaining essentially unchanged. It was popularised in the 1960s with the release of Letraset sheets containing Lorem Ipsum Lorem Ipsum is simply dummy text of the printing and typesetting industry. Lorem Ipsum has been the industry's standard dummy text ever since the 1500s, when an unknown printer took a galley of type and scrambled it to make a type specimen book. It has survived not only five centuries, but also the leap into electronic typesetting, remaining essentially unchanged. It was popularised in the 1960s with the release of Letraset sheets containing Lorem Ipsum Lorem Ipsum is simply dummy text of the printing and typesetting industry. Lorem Ipsum has been the industry's standard dummy text ever since the 1500s, when an unknown printer took a galley of type and scrambled it to make a type specimen book. It has survived not only five centuries, but also the leap into electronic typesetting, remaining essentially unchanged. It was popularised in the 1960s with the release of Letraset sheets containing Lorem Ipsum</p>
  </section>

  <aside class="signin-panel abs">
    <div class="signin-tabs"><span>Register |</span><span class="active">Sign In</span></div>
    <div class="field-light" style="top:34px">
      <svg width="9" height="7" viewBox="0 0 9 7"><rect x=".5" y=".5" width="8" height="6" fill="none" stroke="#999"/><path d="M.5 .5l4 3 4-3" fill="none" stroke="#999"/></svg>Email
    </div>
    <div class="field-light" style="top:67px">
      <svg width="8" height="9" viewBox="0 0 8 9"><rect x="0" y="4" width="8" height="5" fill="#999"/><path d="M2 4V2.5a2 2 0 0 1 4 0V4" fill="none" stroke="#999"/></svg>Password
    </div>
    <span class="forgot-link">Forgot password?</span>
    <span class="signin-button">Sign in</span>
    <div class="or-rule"><span>( or )</span></div>
    <div class="social-button" style="top:144px"><i></i>Login with Kindlebook</div>
    <div class="social-button" style="top:170px"><i></i>Connect with Vornix</div>
    <div class="social-button" style="top:197px"><i></i>Connect with TrellisKey</div>
  </aside>

  <nav class="service-nav abs"></nav>
  <div class="service-tab-active abs"></div>
  <div class="service-item" style="left:249px"><div class="service-icon icon-brand"></div>Who we are ?</div>
  <div class="service-item" style="left:422px">
    <div class="service-icon icon-dark"><svg width="28" height="24" viewBox="0 0 28 24" fill="#d8dde2"><circle cx="14" cy="5" r="4"/><rect x="9" y="10" width="10" height="13" rx="2"/><circle cx="5" cy="8" r="3"/><rect x="1" y="12" width="8" height="10" rx="2"/><circle cx="23" cy="8" r="3"/><rect x="19" y="12" width="8" height="10" rx="2"/></svg></div>Search for<br>a loan</div>
  <div class="service-item" style="left:572px">
    <div class="service-icon icon-light"><svg width="26" height="22" viewBox="0 0 26 22" fill="#2d2d2d"><rect x="4" y="6" width="5" height="12"/><rect x="11" y="2" width="5" height="16"/><rect x="18" y="9" width="5" height="9"/><rect x="1" y="19" width="24" height="2"/></svg></div>Create a<br>payment plan</div>
  <div class="service-item" style="left:711px">
    <div class="service-icon icon-light"><svg width="28" height="22" viewBox="0 0 28 22"><rect x="1" y="2" width="22" height="15" rx="2" fill="#2d2d2d"/><rect x="1" y="5" width="22" height="3" fill="#aaa"/><rect x="16" y="12" width="11" height="9" rx="1" fill="#444" stroke="#fff"/><path d="M18.5 12V9.5a3 3 0 0 1 6 0V12" fill="none" stroke="#444" stroke-width="2"/></svg></div>Make a<br>payment</div>
  <div class="service-item" style="left:846px">
    <div class="service-icon icon-dark"><svg width="28" height="28" viewBox="0 0 28 28" fill="none" stroke="#e6e6e6" stroke-width="2.5"><circle cx="14" cy="14" r="11"/><circle cx="14" cy="14" r="6"/><circle cx="14" cy="14" r="1.5" fill="#e6e6e6"/><path d="M14 14L25 3" stroke-width="1.5"/></svg></div>Practice<br>Management</div>

  <div class="footer-brand abs"><span class="brand-mark"></span><span class="brand-name">LEDGER NEST</span></div>
  <h3 class="footer-title abs" style="left:205px;top:690px">Payment Calculator</h3>
  <span class="field-label abs" style="left:207px;top:723px">Specialty:</span>
  <span class="field-dark abs" style="left:257px;top:721px;width:117px;height:17px"></span>
  <span class="field-label abs" style="left:186px;top:752px">Loan Amount:</span>
  <span class="field-dark abs" style="left:257px;top:751px;width:117px;height:17px"></span>
  <span class="orange-button abs" style="left:304px;top:779px;width:70px;height:17px;line-height:17px">Calculate</span>

  <div class="column-rule abs" style="left:433px"></div>
  <div class="column-rule abs" style="left:725px"></div>

  <h3 class="footer-title abs" style="left:463px;top:659px">Testimonials</h3>
  <span class="quote-mark abs" style="left:456px;top:678px">“</span>
  <div class="testimonial abs" style="top:699px">
    <p>Lorem Ipsum is simply dummy text of the printing and typesetting industry.</p>
    <div class="testimonial-meta"><span>Joe Says</span><span>12-02-2012</span></div>
    <div class="testimonial-more">read more...</div>
  </div>
  <div class="testimonial abs" style="top:753px">
    <p>Lorem Ipsum is simply dummy text of the printing and typesetting industry.</p>
    <div class="testimonial-meta"><span>Joe Says</span><span>12-02-2012</span></div>
    <div class="testimonial-more">read more...</div>
  </div>
  <span class="quote-mark abs" style="left:689px;top:793px">”</span>

  <h3 class="footer-title abs" style="left:752px;top:652px">Quick Contact</h3>
  <span class="field-label abs" style="left:754px;top:685px">Name</span>
  <span class="field-dark abs" style="left:834px;top:680px;width:148px;height:22px"></span>
  <span class="field-label abs" style="left:754px;top:717px">E-mail Address</span>
  <span class="field-dark abs" style="left:834px;top:712px;width:148px;height:22px"></span>
  <span class="field-label abs" style="left:754px;top:749px">Phone number</span>
  <span class="field-dark abs" style="left:834px;top:743px;width:148px;height:22px"></span>
  <span class="field-label abs" style="left:754px;top:782px">Message</span>
  <span class="field-dark abs" style="left:834px;top:775px;width:148px;height:51px"></span>
  <span class="orange-button abs" style="left:993px;top:808px;width:15px;height:15px;border-radius:2px">
    <svg width="15" height="15" viewBox="0 0 15 15"><path d="M3 7.5h8M8 4l3.5 3.5L8 11" fill="none" stroke="#fff" stroke-width="2"/></svg>
  </span>

  <footer class="legal-line abs">Copyright Ledger Nest | Privacy Policy | User Agreement | Terms and Conditions</footer>
</body>
</html>
```